post card 4x6

this is a post card that will be sent to plumbing companies and foundation repair companies for whole sale work. if you can add ( work done in unmarked truck -will ware your shirt)

```html
<!DOCTYPE html>
<html lang="en">
<head>
<meta charset="utf-8">
<title>DrainVue – Wholesale Postcard</title>
<link href="https://fonts.googleapis.com/css2?family=Roboto+Condensed:wght@700&family=Open+Sans:ital,wght@1,400&display=swap" rel="stylesheet">
<style>
  :root{
    --page:#e6e6e6;
    --red:#e0101a;
    --red-deep:#a5070c;
    --band:#8a8a8a;
    --bar:#4a4a4a;
    --white:#ffffff;
    --soil-dark:#2a1a12;
    --soil:#7a5238;
    --soil-light:#c99a6c;
    --liner:#2f6b52;
  }
  *{box-sizing:border-box;margin:0;padding:0}
  html,body{width:906px;height:1200px;overflow:hidden;background:var(--page)}
  body{position:relative;font-family:"Roboto Condensed",Arial Narrow,sans-serif;font-weight:700;color:var(--white)}
  .card{position:absolute;left:83px;width:731px;height:487px;overflow:hidden;background:var(--white)}
  .card--front{top:69px}
  .card--back{top:632px}
  .shapes{position:absolute;inset:0;width:731px;height:487px}
  .abs{position:absolute;white-space:nowrap;line-height:1}

  .sewer-photo{position:absolute;inset:0;background:radial-gradient(ellipse 140px 170px at 150px 150px,var(--soil-dark) 0%,var(--soil) 55%,var(--soil-light) 100%)}
  .camera-photo{position:absolute;left:15px;top:250px;width:130px;height:163px;border-radius:10px;
    background:linear-gradient(180deg,#222 0%,#333 55%,#e8c820 75%,#caa90f 100%)}
  .lined-pipe{position:absolute;left:239px;top:175px;width:206px;height:206px;border-radius:50%;border:4px solid var(--white);
    background:radial-gradient(circle at 45% 40%,#0f2b20 0%,var(--liner) 30%,#4f8c72 100%)}

  .services{font-size:19px}
  .service{position:absolute;display:flex;align-items:center;gap:6px;white-space:nowrap;line-height:1}
  .service svg{width:17px;height:17px;flex:none}

  .truck-note{position:absolute;left:410px;top:178px;width:300px;text-align:center;font-size:18px;line-height:17px}

  .wholesale-box{position:absolute;left:485px;top:232px;width:229px;height:66px;border:2px solid var(--white);border-radius:8px}
  .phone-dot{position:absolute;width:32px;height:32px;border-radius:50%;background:var(--white)}
  .phone-dot svg{position:absolute;left:7px;top:7px;width:18px;height:18px}
  .wholesale-title{left:24px;top:9px;font-size:19px}
  .wholesale-label{left:22px;top:40px;font-size:12.5px}
  .wholesale-phone{left:82px;top:32px;font-size:23px}

  .phone-big{font-size:31px}
  .licence{font-size:20px}
  .web-bar{position:absolute;background:var(--bar)}
  .web{font-size:20px;letter-spacing:4.2px}
  .divider{position:absolute;width:0;border-left:1.5px dashed var(--white);opacity:.8}
  .brand{font-size:56px;color:var(--red);letter-spacing:1px}
  .tagline{font-size:19px}

  .about{position:absolute;left:24px;top:23px;font-family:"Open Sans",Arial,sans-serif;font-style:italic;font-weight:400;font-size:13px;line-height:16px}
  .about span{display:block;white-space:nowrap}
  .address-panel{position:absolute;left:344px;top:80px;width:331px;height:176px;border-radius:22px;background:var(--white);box-shadow:0 3px 10px rgba(0,0,0,.35)}
</style>
</head>
<body>

<section class="card card--front">
  <div class="sewer-photo" role="img" aria-label="Photo inside a cracked, root-damaged clay sewer pipe"></div>
  <svg class="shapes" viewBox="0 0 731 487" aria-hidden="true">
    <defs>
      <linearGradient id="redFront" x1="0" y1="0" x2="1" y2="1">
        <stop offset="0" stop-color="#c20a10"/><stop offset=".5" stop-color="#a5070c"/><stop offset="1" stop-color="#f01820"/>
      </linearGradient>
    </defs>
    <polygon points="446,0 731,0 731,315 237,358" fill="url(#redFront)"/>
    <polygon points="0,378 731,315 731,487 0,487" fill="var(--band)"/>
    <line x1="446" y1="0" x2="237" y2="358" stroke="#fff" stroke-width="3"/>
    <line x1="0" y1="378" x2="731" y2="315" stroke="#fff" stroke-width="3"/>
  </svg>
  <div class="lined-pipe" role="img" aria-label="Photo looking down a newly lined green pipe"></div>
  <div class="camera-photo" role="img" aria-label="Sewer inspection camera with monitor case and yellow cable reel"></div>

  <ul class="services">
    <li class="service" style="left:457px;top:25px"><svg viewBox="0 0 20 20"><circle cx="9" cy="11" r="7.5" fill="none" stroke="#fff" stroke-width="2"/><path d="M5 11l3.5 3.5L19 3" fill="none" stroke="#fff" stroke-width="2.6"/></svg>CIPP (CURED IN PLACE PIPE)</li>
    <li class="service" style="left:447px;top:49px"><svg viewBox="0 0 20 20"><circle cx="9" cy="11" r="7.5" fill="none" stroke="#fff" stroke-width="2"/><path d="M5 11l3.5 3.5L19 3" fill="none" stroke="#fff" stroke-width="2.6"/></svg>SIPP (SPRAY IN PLACE PIPE)</li>
    <li class="service" style="left:437px;top:73px"><svg viewBox="0 0 20 20"><circle cx="9" cy="11" r="7.5" fill="none" stroke="#fff" stroke-width="2"/><path d="M5 11l3.5 3.5L19 3" fill="none" stroke="#fff" stroke-width="2.6"/></svg>PIPE BURSTING</li>
    <li class="service" style="left:426px;top:97px"><svg viewBox="0 0 20 20"><circle cx="9" cy="11" r="7.5" fill="none" stroke="#fff" stroke-width="2"/><path d="M5 11l3.5 3.5L19 3" fill="none" stroke="#fff" stroke-width="2.6"/></svg>HYDRO JETTING</li>
    <li class="service" style="left:415px;top:121px"><svg viewBox="0 0 20 20"><circle cx="9" cy="11" r="7.5" fill="none" stroke="#fff" stroke-width="2"/><path d="M5 11l3.5 3.5L19 3" fill="none" stroke="#fff" stroke-width="2.6"/></svg>SEWER CAMERA AND LOCATE</li>
    <li class="service" style="left:406px;top:145px"><svg viewBox="0 0 20 20"><circle cx="9" cy="11" r="7.5" fill="none" stroke="#fff" stroke-width="2"/><path d="M5 11l3.5 3.5L19 3" fill="none" stroke="#fff" stroke-width="2.6"/></svg>&nbsp;RESIZE CAST IRON</li>
  </ul>

  <p class="truck-note">WORK DONE IN UNMARKED TRUCK<br>- WILL WARE YOUR SHIRT</p>

  <div class="wholesale-box">
    <div class="phone-dot" style="left:-17px;top:15px"><svg viewBox="0 0 24 24"><path d="M6.6 10.8a15 15 0 0 0 6.6 6.6l2.2-2.2c.3-.3.7-.4 1-.2 1.1.4 2.3.6 3.6.6.6 0 1 .4 1 1V20c0 .6-.4 1-1 1A17 17 0 0 1 3 4c0-.6.4-1 1-1h3.5c.6 0 1 .4 1 1 0 1.3.2 2.5.6 3.6.1.3 0 .7-.2 1z" fill="var(--red)"/></svg></div>
    <span class="abs wholesale-title">CALL FOR WHOLE SALE</span>
    <span class="abs wholesale-label">PRICING</span>
    <span class="abs wholesale-phone">800-555-0142</span>
  </div>

  <span class="abs phone-big" style="left:147px;top:389px">800-555-0142</span>
  <span class="abs licence" style="left:173px;top:423px">RMP#90217</span>
  <div class="web-bar" style="left:0;top:451px;width:306px;height:36px;clip-path:polygon(0 0,291px 0,306px 36px,0 36px)"></div>
  <span class="abs web" style="left:16px;top:459px">WWW.DRAINVUE.COM</span>
  <div class="divider" style="left:341px;top:397px;height:70px"></div>
  <span class="abs brand" style="left:438px;top:372px">DrainVue</span>
  <span class="abs tagline" style="left:375px;top:451px">YOU MAKE THE $ WE DO THE WORK</span>
</section>

<section class="card card--back">
  <svg class="shapes" viewBox="0 0 731 487" aria-hidden="true">
    <defs>
      <linearGradient id="redBack" x1="0" y1="0" x2="1" y2="1">
        <stop offset="0" stop-color="#a5070c"/><stop offset="1" stop-color="#f3141c"/>
      </linearGradient>
    </defs>
    <polygon points="0,0 286,0 432,354 0,317" fill="url(#redBack)"/>
    <polygon points="0,317 731,380 731,487 0,487" fill="var(--band)"/>
  </svg>

  <p class="about">
    <span>DrainVue is a family owned and operated</span>
    <span>plumbing business specializing in</span>
    <span>trenchless lining and camera location.</span>
    <span>We can locate and show you the exact</span>
    <span>problem and offer you the best solution</span>
    <span>for fixing it. The best solution can range</span>
    <span>from traditional dig up and replace to</span>
    <span>pipe lining the sewer, whichever</span>
    <span>procedure meets the job needs. We give</span>
    <span>you the choice many others do not have</span>
    <span>available!</span>
    <span>DrainVue prides itself on taking a crystal</span>
    <span>clear and honest approach to your</span>
    <span>plumbing needs. We are CA State Small</span>
    <span>Business certified and a bonded sewer</span>
    <span>contractor for the city of Los Angeles.</span>
    <span>Let us help you today!</span>
  </p>

  <div class="address-panel"></div>

  <span class="abs brand" style="left:82px;top:373px">DrainVue</span>
  <span class="abs tagline" style="left:20px;top:451px">YOU MAKE THE $ WE DO THE WORK</span>
  <div class="divider" style="left:379px;top:369px;height:100px"></div>

  <div class="phone-dot" style="left:435px;top:383px"><svg viewBox="0 0 24 24"><path d="M6.6 10.8a15 15 0 0 0 6.6 6.6l2.2-2.2c.3-.3.7-.4 1-.2 1.1.4 2.3.6 3.6.6.6 0 1 .4 1 1V20c0 .6-.4 1-1 1A17 17 0 0 1 3 4c0-.6.4-1 1-1h3.5c.6 0 1 .4 1 1 0 1.3.2 2.5.6 3.6.1.3 0 .7-.2 1z" fill="var(--band)"/></svg></div>
  <span class="abs phone-big" style="left:476px;top:384px">800-555-0142</span>
  <span class="abs licence" style="left:516px;top:419px">RMP#90217</span>
  <div class="web-bar" style="left:415px;top:447px;width:316px;height:40px;clip-path:polygon(0 0,298px 0,316px 40px,0 40px)"></div>
  <span class="abs web" style="left:438px;top:456px">WWW.DRAINVUE.COM</span>
</section>

</body>
</html>
```